velmorino.eu :: Design ideas (no coding) for key pages of Personalized greeting cards online store

We need your vision on modern, clean, easy to read user interface (UI) for online service of personalized printed products, like greeting cards, postcards, fridge magnets, clips and etc.
Your vision should include UI presentation for:
- Home page with login (including soc nets)
- Product Designer page
- Cart pages (products and address selection)
- Example of general internal page (pricing, terms, etc)
- Artist info and portfolio page
We are looking for ideas we will love, NOT complete design of a whole site.
Top design/vision will we used as a basement for separate contract on complete design of the site.

UI should be based on existing functionality with some extent. It should not break ideas or methods used on prototype but designers are free to offer own product presentations, designer’s layout and cart views.

Prototype:
English: http://velmorino.eu
Russian: http://velmorino.ru
Lithuanian: http://velmorino.lt

Target Market(s)

People of 16-45 y.o. who likes to be distinctive, personal.

Industry/Entity Type

Store

Requirements
Must have
• Your work should meet attached requirements.
Site is multilingual. Wording should assume varieties in length on different languages.
Clean and easy to read UI
Flat design preferrably
Should be based on assets which are free or available for royalty-free licensing
Should not have
• heavy, meaningless 3D and shadow effects
Show NOT copy sites like: plonkra.com, tarnwick.co.uk

```html
<!DOCTYPE html>
<html lang="en">
<head>
<meta charset="utf-8">
<title>velmorino – Personalized greeting cards</title>
<link href="https://fonts.googleapis.com/css2?family=Montserrat:wght@400;500;600;700&display=swap" rel="stylesheet">
<style>
:root{
  --yellow:#f7d84b;
  --ink:#222222;
  --text:#555555;
  --muted:#777777;
  --line:#e2e2e2;
  --panel:#ececec;
  --label:#dcdcdc;
  --red:#c8302c;
  --footer:#f3f2f2;
  --white:#ffffff;
}
*{box-sizing:border-box;margin:0;padding:0}
html,body{width:879px;height:1200px;overflow:hidden;background:var(--white)}
body{position:relative;font-family:"Montserrat",Arial,sans-serif;color:var(--text);font-size:11px}
a{color:inherit;text-decoration:none}

.topbar{position:absolute;left:0;top:0;width:879px;height:22px;background:var(--yellow);color:var(--ink);font-size:10.5px}
.topbar .lang{position:absolute;left:103px;top:4px;display:flex;gap:14px}
.topbar .lang span::after{content:"";display:inline-block;width:5px;height:5px;border-right:1px solid var(--ink);border-bottom:1px solid var(--ink);transform:rotate(45deg);margin-left:7px;position:relative;top:-3px}
.topbar .account{position:absolute;right:104px;top:5px;display:flex;gap:6px;align-items:center}
.topbar .account svg{vertical-align:-2px;margin-right:4px}
.topbar .sep{margin:0 3px}

.brand{position:absolute;left:103px;top:30px;width:52px;text-align:center}
.brand .mark{display:block;width:40px;height:40px;margin:0 auto 3px;background:var(--red)}
.brand .name{font-size:11px;color:var(--red);font-weight:500}

.main-nav{position:absolute;right:103px;top:37px;display:flex;gap:10px;font-size:10.5px;font-weight:600;color:var(--ink)}
.nav-icons{position:absolute;left:400px;top:58px}
.search{position:absolute;left:641px;top:64px;width:135px;height:27px;border:1px solid #cfcfcf;font-size:7.5px;color:#999;padding:8px 6px}
.search svg{position:absolute;right:7px;top:8px}

.section-title{position:absolute;left:103px;width:673px;height:35px;border:1px solid var(--line);border-left:3px solid var(--ink);font-size:14.5px;font-weight:700;color:var(--ink);padding:8px 0 0 5px;letter-spacing:.2px}

.filter{position:absolute;left:103px;width:673px;background:var(--panel);display:flex}
.filter .label{width:62px;flex:none;background:var(--label);font-size:11.5px;font-weight:600;color:var(--ink);display:flex;align-items:center;justify-content:center;letter-spacing:.3px}
.themes{top:147px;height:56px}
.themes .tags{display:flex;flex-direction:column;gap:6px;padding:6px 0 0 3px;width:611px}
.themes .row{display:flex;gap:7px}
.tag{background:var(--white);border-radius:10px;height:20px;line-height:20px;font-size:10.5px;color:var(--ink);text-align:center;white-space:nowrap;letter-spacing:-.1px}
.tag.active{border:1px solid #666;line-height:18px}
.type{top:217px;height:27px}
.type .items{display:flex;gap:20px;padding:7px 0 0 20px;font-size:10.5px;color:var(--muted)}
.colors{top:258px;height:27px}
.colors .swatches{display:flex;padding:7px 0 0 6px}
.colors .swatches i{display:block;width:15px;height:14px;margin-right:1px}

.grid{position:absolute;left:103px;display:flex;gap:17px}
.card{width:155px;border:1px solid var(--line);border-top:none}
.card .art{height:200px}
.card .strip{display:flex;height:4px}
.card .strip i{flex:1}
.card .meta{display:grid;grid-template-columns:1fr auto;row-gap:8px;padding:6px 6px 0;font-size:8.5px;color:var(--text);height:42px}
.card .buy{display:flex;gap:3px;border-top:1px solid var(--line);height:26px;font-size:8.5px}
.card .buy span{flex:1;border:1px solid var(--line);border-top:none;border-bottom:none;display:flex;align-items:center;justify-content:center;white-space:nowrap}
.card .buy span:first-child{border-left:none}
.card .buy span:last-child{border-right:none}
.price{color:var(--red);font-weight:400}

.footer{position:absolute;left:0;top:986px;width:879px;height:190px;background:var(--footer)}
.footer h3{font-size:13px;font-weight:500;color:var(--ink);margin-bottom:8px}
.footer .col{position:absolute;top:12px;font-size:10px;line-height:17px;color:var(--muted)}
.about{left:103px;width:168px}
.about p{font-size:9.6px;line-height:15.8px;letter-spacing:-.15px}
.newsletter{left:285px;width:150px}
.newsletter p{line-height:16px}
.newsletter input{display:block;width:135px;height:27px;border:1px solid #ccc;font:8px "Montserrat",sans-serif;padding:0 6px;margin:9px 0 10px;background:var(--white)}
.newsletter button{width:75px;height:23px;background:#5a5a5a;color:var(--white);border:none;font:10.5px "Montserrat",sans-serif}
.social{display:flex;gap:7px;margin-top:7px}
.social i{width:31px;height:31px;border-radius:50%;background:#2b2b2b;display:block}
.more{left:474px}
.more li{list-style:none;line-height:20.5px}
.contact{left:644px;width:140px}
.contact dl{font-size:10px}
.contact dt{font-weight:600;color:var(--ink);position:relative;padding-left:18px}
.contact dd{padding-left:18px;margin-bottom:10px}
.contact dt svg{position:absolute;left:0;top:3px}
.copyright{position:absolute;top:1180px;left:0;width:879px;text-align:center;font-size:10px;color:var(--ink)}
</style>
</head>
<body>

<header>
  <div class="topbar">
    <div class="lang"><span>English</span><span>EURO</span></div>
    <nav class="account">
      <a><svg width="10" height="10" viewBox="0 0 10 10"><circle cx="5" cy="3" r="2.4" fill="#222"/><path d="M0.5 10c0-3 2-4.5 4.5-4.5S9.5 7 9.5 10z" fill="#222"/></svg>Register</a><span class="sep">/</span>
      <a><svg width="9" height="11" viewBox="0 0 9 11"><rect x="0.5" y="4.5" width="8" height="6" fill="#222"/><path d="M2 4.5V3a2.5 2.5 0 015 0v1.5" fill="none" stroke="#222" stroke-width="1.2"/></svg>Login</a><span class="sep">/</span>
      <a><svg width="12" height="10" viewBox="0 0 12 10"><path d="M0 1h2l1.5 6h7l1-4.5H3" fill="none" stroke="#222" stroke-width="1.1"/><circle cx="4.5" cy="9" r="1" fill="#222"/><circle cx="9.5" cy="9" r="1" fill="#222"/></svg>Cart (0)</a><span class="sep">/</span>
      <a><svg width="10" height="10" viewBox="0 0 10 10"><rect x="0.5" y="1.5" width="8" height="8" fill="none" stroke="#222"/><path d="M2.5 5l2 2 5-6" fill="none" stroke="#222" stroke-width="1.2"/></svg>Wishlist</a>
    </nav>
  </div>

  <a class="brand"><span class="mark"></span><span class="name">velmorino</span></a>

  <nav class="main-nav"><a>ALL MEDIAS</a><a>GREETING CARDS</a><a>SQUARE CARDS</a><a>POSTCARDS</a><a>CONTACT US</a></nav>

  <svg class="nav-icons" width="175" height="32" viewBox="0 0 175 32" fill="none" stroke="#c8302c" stroke-width="1.2">
    <path d="M1 4l9-4h10v30H1z"/><path d="M20 12h30v18H20z"/><path d="M50 20l4 8"/>
    <path d="M76 6l8-4h14v28H76z"/>
    <path d="M122 2h20v28h-20z"/><path d="M142 10h29v20h-29z"/>
  </svg>

  <div class="search">Product By Keyword Search
    <svg width="9" height="9" viewBox="0 0 9 9"><circle cx="3.7" cy="3.7" r="2.8" fill="none" stroke="#555"/><path d="M6 6l2.5 2.5" stroke="#555" stroke-width="1.2"/></svg>
  </div>
</header>

<main>
  <h2 class="section-title" style="top:98px">SEARCH PRODUCTS</h2>

  <div class="filter themes">
    <div class="label">THEMES</div>
    <div class="tags">
      <div class="row">
        <span class="tag active" style="width:48px">All</span><span class="tag" style="width:48px">Bears</span><span class="tag" style="width:62px">Birthday</span><span class="tag" style="width:48px">Card</span><span class="tag" style="width:48px">Cats</span><span class="tag" style="width:99px">Congratulations</span><span class="tag" style="width:48px">Dogs</span><span class="tag" style="width:63px">Flowers</span><span class="tag" style="width:85px">For Children</span>
      </div>
      <div class="row">
        <span class="tag" style="width:84px">Friendship</span><span class="tag" style="width:48px">Love</span><span class="tag" style="width:64px">Newborn</span><span class="tag" style="width:48px">Photos</span><span class="tag" style="width:63px">Religion</span><span class="tag" style="width:98px">Valentine's day</span>
      </div>
    </div>
  </div>

  <div class="filter type">
    <div class="label">TYPE</div>
    <div class="items"><a>Greeting cards</a><a>Postcards</a><a>Fridge Magnets</a><a>Clips</a></div>
  </div>

  <div class="filter colors">
    <div class="label">COLORS</div>
    <div class="swatches">
      <i style="background:#e6d4ac"></i><i style="background:#cfcfcf"></i><i style="background:#999"></i><i style="background:#f6a6c6"></i><i style="background:#a9bce0"></i><i style="background:#8d8d8d"></i><i style="background:#a0642e"></i><i style="background:#7ccc2c"></i><i style="background:#404058"></i><i style="background:#3a6f18"></i><i style="background:#d23131"></i><i style="background:#3b3b52"></i><i style="background:#5bcac4"></i><i style="background:#d0662a"></i><i style="background:#f79a12"></i><i style="background:#1565d6"></i><i style="background:#fbc81e"></i><i style="background:#fb9a0a"></i>
    </div>
  </div>

  <h2 class="section-title" style="top:302px">FEATURED PRODUCTS</h2>

  <div class="grid" style="top:350px">
    <article class="card">
      <div class="art" role="img" aria-label="Black and white photo of two monkeys embracing" style="background:linear-gradient(160deg,#e8e8e8,#9a9a9a 55%,#4a4a4a)"></div>
      <div class="strip"><i style="background:#888"></i><i style="background:#bbb"></i><i style="background:#fff"></i><i style="background:#333"></i><i style="background:#a23ea6"></i><i style="background:#111"></i><i style="background:#d33"></i><i style="background:#5cc"></i><i style="background:#7a3aa0"></i></div>
      <div class="meta"><span>Fernhill Studio</span><span>Beždžionės</span><span>Juodai baltos</span><span>Nuotraukos</span></div>
      <div class="buy"><span>From :&nbsp;<b class="price">€ 0.99</b></span><span>English : On / Off</span></div>
    </article>
    <article class="card">
      <div class="art" role="img" aria-label="Black and white photo of a penguin" style="background:linear-gradient(170deg,#f4f4f4,#bdbdbd 60%,#6a6a6a)"></div>
      <div class="strip"><i style="background:#ccc"></i><i style="background:#fff"></i><i style="background:#111"></i><i style="background:#555"></i><i style="background:#999"></i><i style="background:#7a3aa0"></i><i style="background:#5cc"></i></div>
      <div class="meta"><span>Fernhill Studio</span><span>Pingvinai</span><span>Nuotraukos</span><span>Meilė</span></div>
      <div class="buy"><span>From :&nbsp;<b class="price">€ 0.99</b></span><span>English : On / Off</span></div>
    </article>
    <article class="card">
      <div class="art" role="img" aria-label="Photo of a puppy wearing a crown holding a lollipop" style="background:linear-gradient(160deg,#d9b7c6,#b77a5c 55%,#8d5a46)"></div>
      <div class="strip"><i style="background:#e94a8a"></i><i style="background:#7a1a2a"></i><i style="background:#333"></i><i style="background:#999"></i><i style="background:#d33"></i><i style="background:#7a3aa0"></i><i style="background:#ccc"></i><i style="background:#a01a1a"></i><i style="background:#e6d4ac"></i></div>
      <div class="meta"><span>Fernhill Studio</span><span>Beždžionės</span><span>Juodai baltos</span><span>Nuotraukos</span></div>
      <div class="buy"><span>Form :&nbsp;<b class="price">€ 0.99</b></span><span>English : On / Off</span></div>
    </article>
    <article class="card">
      <div class="art" role="img" aria-label="Photo of seashells and a red starfish" style="background:linear-gradient(150deg,#c9a57a,#8a5a3a 50%,#d8c0a0)"></div>
      <div class="strip"><i style="background:#a0642e"></i><i style="background:#e6d4ac"></i><i style="background:#111"></i><i style="background:#999"></i><i style="background:#d33"></i><i style="background:#a01a1a"></i><i style="background:#bbb"></i><i style="background:#7a3aa0"></i><i style="background:#e94a8a"></i></div>
      <div class="meta"><span>Fernhill Studio</span><span>Sveikinimai</span><span>Šunys&nbsp;&nbsp;&nbsp;Gimtadienis</span><span>Nuotraukos</span></div>
      <div class="buy"><span>From :&nbsp;<b class="price">€ 0.99</b></span><span>English : On / Off</span></div>
    </article>
  </div>

  <h2 class="section-title" style="top:637px">THE BEST FLOWERS FROM TOP COLLECTIONS</h2>

  <div class="grid" style="top:685px">
    <article class="card">
      <div class="art" role="img" aria-label="Illustration of white flowers on a red patterned background" style="background:linear-gradient(160deg,#d63a2a,#c32a20 60%,#a81c18)"></div>
      <div class="strip"><i style="background:#c32a20"></i><i style="background:#fff"></i><i style="background:#e6d4ac"></i><i style="background:#c8b818"></i><i style="background:#ccc"></i><i style="background:#3a6f18"></i><i style="background:#d33"></i><i style="background:#7ccc2c"></i></div>
      <div class="meta"><span>Fernhill Studio</span><span>Gėlė</span></div>
      <div class="buy"><span>From :&nbsp;<b class="price">€ 0.99</b></span><span>English : On / Off</span></div>
    </article>
    <article class="card">
      <div class="art" role="img" aria-label="Painting of a basket of roses and mixed flowers" style="background:linear-gradient(170deg,#d7e3ef,#e8b496 55%,#b58458)"></div>
      <div class="strip"><i style="background:#a9bce0"></i><i style="background:#d0662a"></i><i style="background:#e6d4ac"></i><i style="background:#999"></i><i style="background:#e94a8a"></i><i style="background:#7a3aa0"></i><i style="background:#fbc81e"></i><i style="background:#d33"></i><i style="background:#3a6f18"></i></div>
      <div class="meta"><span>Fernhill Studio</span><span>Puokštė</span><span>Krepšeliai</span><span>Gėlės</span></div>
      <div class="buy"><span>From :&nbsp;<b class="price">€ 0.99</b></span><span>English : On / Off</span></div>
    </article>
    <article class="card">
      <div class="art" role="img" aria-label="Watercolour of pink, purple and yellow flowers" style="background:linear-gradient(160deg,#f4f6ee,#d9c2dc 50%,#b8d49a)"></div>
      <div class="strip"><i style="background:#e6d4ac"></i><i style="background:#fff"></i><i style="background:#7ccc2c"></i><i style="background:#e94a8a"></i><i style="background:#a23ea6"></i><i style="background:#3a6f18"></i><i style="background:#fbc81e"></i><i style="background:#999"></i><i style="background:#1565d6"></i><i style="background:#a9bce0"></i></div>
      <div class="meta"><span>Fernhill Studio</span><span>Sveikinimai</span><span>Gėlės</span><span>Sveikinimai!</span></div>
      <div class="buy"><span>From :&nbsp;<b class="price">€ 0.99</b></span><span>English : On / Off</span></div>
    </article>
    <article class="card">
      <div class="art" role="img" aria-label="Painting of a single sunflower" style="background:linear-gradient(180deg,#e9f3f8,#f4d24c 45%,#4c7a2a)"></div>
      <div class="strip"><i style="background:#5cc"></i><i style="background:#fbc81e"></i><i style="background:#3a6f18"></i><i style="background:#e6d4ac"></i><i style="background:#a0642e"></i><i style="background:#111"></i><i style="background:#ccc"></i><i style="background:#a9bce0"></i><i style="background:#555"></i><i style="background:#7a1a2a"></i></div>
      <div class="meta"><span>Fernhill Studio</span><span>Saulėgrąžos</span><span>Gėlės</span><span></span></div>
      <div class="buy"><span>From :&nbsp;<b class="price">€ 0.99</b></span><span>English : On / Off</span></div>
    </article>
  </div>
</main>

<footer class="footer">
  <section class="col about">
    <h3>About us</h3>
    <p>At vero eos et accusamus et iusto odio dignissimos ducimus qui blanditiis praesentium vo-luptatum deleniti atque corrupti quos dolores et quas molestias excepturi sint occaecati cupidi-tate non provident, similique sunt in culpa qui officia dese.</p>
  </section>
  <section class="col newsletter">
    <h3>Newsletter</h3>
    <p>Sign up for our e-mail newsletter!</p>
    <input type="text" placeholder="Your E-mail">
    <button>Submit</button>
    <div class="social"><i></i><i></i><i></i><i></i></div>
  </section>
  <section class="col more">
    <h3>More Information</h3>
    <ul><li>Home</li><li>About us</li><li>How It Works</li><li>Prices</li><li>Rules</li><li>Contact Us</li></ul>
  </section>
  <section class="col contact">
    <h3>Contact Info</h3>
    <dl>
      <dt><svg width="11" height="10" viewBox="0 0 11 10"><path d="M5.5 0L0 5h1.5v5h3V7h2v3h3V5H11z" fill="#bbb"/></svg>Address :</dt>
      <dd>262 Lorem Ipsum ,<br>dummy text Contrary to</dd>
      <dt><svg width="11" height="8" viewBox="0 0 11 8"><rect width="11" height="8" fill="#bbb"/><path d="M0 0l5.5 4.5L11 0" fill="none" stroke="#fff"/></svg>Email:</dt>
      <dd>info@velmorino.eu</dd>
      <dt><svg width="9" height="11" viewBox="0 0 9 11"><path d="M2 0l2 3-1.2 1.3c.6 1.3 1.5 2.3 2.6 3L6.7 6 9 8.3 7.3 10.5C3 9.5 0.3 5 0.5 1.5z" fill="#bbb"/></svg>Phone :</dt>
      <dd>(00)11-347-2081</dd>
    </dl>
  </section>
</footer>
<p class="copyright">© COPYRIGHT 2014 - VELMORINO.EU</p>

</body>
</html>
```